Professional, polished website design for boutique wealth management firm

Hello, thank you for your interest. PLEASE READ THE BRIEF BEFORE SUBMITTING THE DESIGN.-
PLEASE USE THE ATTACHED HOME PAGE COPY FOR THIS DESIGN.
We are looking for a professional, polished design that helps portray trust and credibility for a well-established independent wealth management firm. We have copy we've written for the home page and we'd like the design and imagery to play up the copy, so there's a better chance someone will read it all. So the headlines etc should all be easy to read and the design should draw the eye towards them. For colors, again trust is important so probably blue as a dominant color, but you can also use gray, green, etc. We'd like to avoid too much use of the color red (due to financial, association with loss). SO PLEASE AVOID USE OF THE COLOR RED. We also like bright orange or yellow for call to action buttons.

Please keep the design EASY TO MAINTAIN in wordpress as well.

I have attached home page copy as well as logo files.

Here's some sites that we like so feel free to use as inspiration:
https://www.brovaltcapitalworks.example/, https://harborpathpensionsplains.example/
https://tavrin-oakes.example/, https://plantfornextyear.example/, https://ferngatefinancial.example/

As another option/idea, I like the idea of a simple format with a clean image similar to this for the home page: https://www.pixmeadowstock.example/detail/photo/calculator-falling-royalty-free-image/31684207?adppopup=true
Just an idea.

Also please be sure to incorporate the QWA /Accredited Wealth Steward logo as well, farther down the page is fine.

Thank you for your help! Feel free to contact me with any questions.

Target Market(s)

Individuals aged 48-62 who are looking to maximize their wealth, such as business owners, executives, engineers, successful tradespeople, etc.

Industry/Entity Type

Finance--wealth management

Font styles to use
Sans Serif

Requirements
Must have
• Professional and polished, Call to action buttons must be clear and stand out, headlines must be clear and stand out, also text must be big enough to be easily readable by most people
Should not have
• Anything casual, frilly, etc.

```html
<!DOCTYPE html>
<html lang="en">
<head>
<meta charset="utf-8">
<title>Stellan Asset Advisors</title>
<link rel="stylesheet" href="https://fonts.googleapis.com/css2?family=Poppins:wght@400;500;600;700&display=swap">
<style>
:root{
  --navy:#2b3a97;
  --navy-deep:#1f2c80;
  --ink:#1d2561;
  --text:#3a3f55;
  --white:#ffffff;
  --stage:#f1f2f6;
  --footer:#141a3a;
  --line-light:rgba(255,255,255,.75);
  --dash:#6d76b8;
}
*{box-sizing:border-box;margin:0;padding:0}
html,body{width:1200px;height:4247px;overflow:hidden}
body{position:relative;background:var(--stage);font-family:"Poppins",sans-serif;color:var(--text)}
.abs{position:absolute}
.page{left:33px;top:30px;width:1135px;height:4158px;background:var(--white);box-shadow:0 10px 40px rgba(20,26,58,.18);overflow:hidden}
.nav{left:33px;top:30px;width:1135px;height:54px;background:var(--white);z-index:3}
.brand{display:flex;align-items:center;gap:8px;font-weight:600;color:var(--navy);font-size:20px;letter-spacing:.5px}
.brand-dot{width:22px;height:22px;border-radius:50%;background:var(--navy)}
.menu{display:flex;gap:40px;font-size:12px;color:var(--ink);font-weight:500}
.hero-photo{left:33px;top:84px;width:1135px;height:540px;background:radial-gradient(ellipse at 20% 30%,#ffffff 0%,#f1f5fb 35%,rgba(241,245,251,0) 60%),linear-gradient(110deg,#f4f7fc 0%,#e6edf8 45%,#d3ddee 70%,#b9c6de 100%)}
.hero-object{left:560px;top:140px;width:560px;height:400px;border-radius:40px;transform:rotate(28deg);background:linear-gradient(160deg,#fbfcfe 0%,#e3e7ee 45%,#a9b1c0 100%);box-shadow:0 20px 40px rgba(40,50,90,.18)}
.hero-title{left:221px;top:202px;width:400px;font-size:29px;line-height:34.5px;font-weight:700;color:var(--navy-deep);text-transform:uppercase}
.hero-copy{left:221px;top:328px;width:352px;font-size:10px;line-height:12.5px;color:var(--ink)}
.btn{display:inline-flex;align-items:center;justify-content:center;background:var(--navy);color:var(--white);border-radius:16px;font-size:11.5px;font-weight:500}
.h2{font-weight:700;color:var(--navy-deep);font-size:19px;line-height:22px}
.body{font-size:11.5px;line-height:17.5px}
.circle{border-radius:50%;border:7px solid var(--navy);overflow:hidden}
.photo{width:100%;height:100%}
.band-title{width:700px;left:251px;text-align:center;color:var(--white);font-weight:600;font-size:18px;line-height:22px}
.band-sub{width:700px;left:251px;text-align:center;color:var(--white);font-size:11px}
.item-title{color:var(--white);font-weight:500;font-size:16px}
.item-copy{color:var(--white);font-size:11px;line-height:17.5px;width:305px}
.timeline{left:600px;top:1389px;width:0;height:1041px;border-left:2px dashed var(--line-light)}
.node{width:44px;height:44px;border-radius:50%;border:2px dashed var(--line-light);background:var(--navy);display:flex;align-items:center;justify-content:center}
.node::after{content:"";width:10px;height:10px;border-radius:50%;background:var(--white)}
.end-dot{width:10px;height:10px;border-radius:50%;background:var(--white)}
.service{width:160px;text-align:center;font-size:12px;font-weight:500;color:var(--ink);line-height:15px}
.service-icon{width:68px;height:68px;border-radius:50%;border:2px solid var(--navy);margin:0 auto 10px;display:flex;align-items:center;justify-content:center;background:var(--white)}
.hub{left:521px;top:2837px;width:160px;height:160px;border-radius:50%;border:3px solid var(--navy);display:flex;align-items:center;justify-content:center;color:var(--navy);font-weight:600;font-size:18px;background:var(--white)}
.footer-copy{left:351px;top:4005px;width:500px;text-align:center;color:var(--white);font-size:11.5px;line-height:18px}
.social{display:flex;gap:14px}
.social span{width:13px;height:13px;border-radius:50%;background:var(--white)}
</style>
</head>
<body>
<div class="abs page"></div>

<header class="abs nav">
  <div class="abs brand" style="left:189px;top:14px"><span class="brand-dot"></span>Stellan</div>
  <nav class="abs menu" style="left:630px;top:20px"><span>Home</span><span>About Us</span><span>Our Team</span><span>Contact Us</span></nav>
</header>

<!-- Hero -->
<div class="abs hero-photo" role="img" aria-label="Soft-focus office backdrop"></div>
<div class="abs hero-object" role="img" aria-label="Desk calculator held in a hand"></div>
<svg class="abs" style="left:33px;top:500px" width="1135" height="130" viewBox="0 0 1135 130" preserveAspectRatio="none">
  <path d="M0 30 C200 140 420 60 620 80 C820 100 960 10 1135 40 L1135 130 L0 130Z" fill="#ffffff"/>
</svg>
<h1 class="abs hero-title">The most effective financial plans start with tax planning.</h1>
<p class="abs hero-copy">Few financial advisors offer tax expertise, but when they do, you benefit.&nbsp; Learn how our unique team combines financial planning, investments and smart tax and incomegeneration strategies to help you achieve your goals faster.</p>
<a class="abs btn" style="left:221px;top:411px;width:178px;height:29px">Learn why we’re different</a>

<!-- Intro -->
<div class="abs circle" style="left:231px;top:672px;width:358px;height:358px">
  <div class="photo" role="img" aria-label="Advisors meeting around a conference table" style="background:linear-gradient(135deg,#dfe6ef,#8fa2bb 60%,#4a5a78)"></div>
</div>
<h2 class="abs h2" style="left:631px;top:734px;width:350px;font-size:16.5px;line-height:21px">Cookie-cutter financial planning and investment can leave your future at risk.&nbsp; That’s why we do it differently.</h2>
<p class="abs body" style="left:631px;top:818px;width:345px;font-size:11px;line-height:17.5px;color:var(--ink)">You need better strategies in today’s complex financial landscape.At Stellan Asset Advisors, we bring financial planning, investment management, retirement income, tax and estate planning expertisetogether under one roof. Our unique team works together to help you make the most of your resources.</p>
<a class="abs btn" style="left:631px;top:945px;width:170px;height:29px">Learn why we’re different</a>

<!-- Blue band -->
<svg class="abs" style="left:33px;top:1110px" width="1135" height="1500" viewBox="0 0 1135 1500" preserveAspectRatio="none">
  <path d="M0 60 C260 60 420 0 620 20 C820 40 950 0 1135 12 L1135 1440 C950 1470 820 1420 620 1430 C420 1440 220 1500 0 1480Z" fill="#2b3a97"/>
</svg>
<h2 class="abs band-title" style="top:1245px">Better strategies to preserve and grow wealth,<br>generate income and reduce your taxes</h2>
<p class="abs band-sub" style="top:1305px">Here’s what you can expect when you work with Stellan.</p>

<div class="abs timeline"></div>
<div class="abs end-dot" style="left:596px;top:1370px"></div>
<div class="abs end-dot" style="left:596px;top:2393px"></div>
<div class="abs node" style="left:579px;top:1511px"></div>
<div class="abs node" style="left:579px;top:1855px"></div>
<div class="abs node" style="left:579px;top:2182px"></div>

<h3 class="abs item-title" style="left:219px;top:1450px">A Better Approach</h3>
<p class="abs item-copy" style="left:219px;top:1490px">Taxes are critical to every financial move you make, so we incorporate tax planning in everything we do for you.&nbsp; Along with managing your investments, we help you safely generate retirement income, reduce capital gains and minimize income taxes.&nbsp; We’ll also help you with estate planning strategies so you can protect your family’s future and make the most of opportunities.</p>
<div class="abs circle" style="left:653px;top:1393px;width:318px;height:300px;border-color:#fff">
  <div class="photo" role="img" aria-label="Advisor talking with a client at a laptop" style="background:linear-gradient(135deg,#eef1f5,#b9c4d4 55%,#5b6a85)"></div>
</div>

<div class="abs circle" style="left:221px;top:1724px;width:300px;height:292px;border-color:#fff">
  <div class="photo" role="img" aria-label="Magnifying glass over stacks of coins" style="background:radial-gradient(circle at 60% 55%,#c9a456,#6f5a2e 35%,#173a5e 70%,#0f2744)"></div>
</div>
<h3 class="abs item-title" style="left:654px;top:1793px">More Experience</h3>
<p class="abs item-copy" style="left:654px;top:1830px">You’ve worked hard to get where you are, so your money shouldn’t have to be part of anyone’s learning curve.&nbsp; At Stellan Asset Advisors, you’ll only work with seasoned experts, each with decades of investment, planning or tax experience.&nbsp; Our team works together to help solve your financial challenges and get your money working harder for you.</p>

<h3 class="abs item-title" style="left:219px;top:2131px">On Your Side</h3>
<p class="abs item-copy" style="left:219px;top:2165px">In an industry rife with conflicts of interest, you need a firm that works in your best interest.&nbsp; As an independent firm, we have noties to insurance or mutual fund companies.&nbsp; We’re fee-based,meaning we’re compensated by fees, not commissions.&nbsp; We also act as your fiduciary, so we’re ethically bound to put your interests first.&nbsp; That way, you get our best advice...not product recommendations.</p>
<div class="abs circle" style="left:653px;top:2058px;width:318px;height:300px;border-color:#fff">
  <div class="photo" role="img" aria-label="Couple reviewing paperwork together" style="background:linear-gradient(135deg,#f1ece6,#c7b7a6 55%,#6b5a4c)"></div>
</div>

<!-- Services -->
<h2 class="abs h2" style="left:351px;top:2626px;width:500px;text-align:center;font-size:17.5px">Personalized solutions to help your<br>money work harder for you</h2>
<svg class="abs" style="left:0;top:2840px" width="1200" height="300" viewBox="0 0 1200 300">
  <g stroke="#6d76b8" stroke-width="1.3" stroke-dasharray="4 4" fill="none">
    <line x1="352" y1="42" x2="490" y2="78"/>
    <line x1="352" y1="192" x2="490" y2="142"/>
    <line x1="850" y1="42" x2="712" y2="78"/>
    <line x1="850" y1="192" x2="712" y2="142"/>
    <line x1="601" y1="157" x2="601" y2="282"/>
  </g>
</svg>
<div class="abs hub">Stellan</div>

<div class="abs service" style="left:232px;top:2820px">
  <div class="service-icon"><svg width="30" height="30" viewBox="0 0 30 30" fill="none" stroke="#2b3a97" stroke-width="1.8"><circle cx="15" cy="15" r="10"/><path d="M18 11h-4a2 2 0 000 4h2a2 2 0 010 4h-4M15 8v3M15 19v3"/></svg></div>
  Investment<br>Management</div>
<div class="abs service" style="left:232px;top:2975px">
  <div class="service-icon"><svg width="30" height="30" viewBox="0 0 30 30" fill="none" stroke="#2b3a97" stroke-width="1.8"><rect x="6" y="5" width="18" height="20" rx="2"/><path d="M10 11h10M10 15h10M10 19h6"/></svg></div>
  Tax Planning</div>
<div class="abs service" style="left:800px;top:2820px">
  <div class="service-icon"><svg width="30" height="30" viewBox="0 0 30 30" fill="none" stroke="#2b3a97" stroke-width="1.8"><path d="M8 4h10l5 5v17H8z"/><path d="M11 21l3-4 3 2 3-5"/></svg></div>
  Comprehensive<br>Financial Planning</div>
<div class="abs service" style="left:800px;top:2975px">
  <div class="service-icon"><svg width="30" height="30" viewBox="0 0 30 30" fill="none" stroke="#2b3a97" stroke-width="1.8"><rect x="6" y="6" width="18" height="18" rx="2"/><path d="M10 20v-5M15 20v-8M20 20v-3"/></svg></div>
  Estate Planning</div>
<div class="abs service" style="left:518px;top:3085px">
  <div class="service-icon"><svg width="30" height="30" viewBox="0 0 30 30" fill="none" stroke="#2b3a97" stroke-width="1.8"><rect x="5" y="9" width="20" height="14" rx="2"/><path d="M10 9V6h10v3M5 15h20"/></svg></div>
  Retirement<br>Income Planning</div>

<!-- Check-up -->
<div class="abs circle" style="left:209px;top:3282px;width:358px;height:358px">
  <div class="photo" role="img" aria-label="Senior couple reviewing finances on a sofa" style="background:linear-gradient(135deg,#e9e2d6,#b3a58f 50%,#4f5a4a)"></div>
</div>
<h2 class="abs h2" style="left:615px;top:3323px;width:400px;font-size:17.5px">The Stellan $549 Retirement Check-Up</h2>
<p class="abs body" style="left:615px;top:3370px;width:362px;font-size:11px;color:var(--ink)">We know it’s a big decision to hire or switch advisors. That’s why we provide an easy way to try us out.&nbsp; At the same time, you can get a valuable second opinion to find out if you’re on track to retire. There’s no pressure, and either way, you’ll walk away with valuable insights on what you should be doing to secure your future.</p>
<a class="abs btn" style="left:615px;top:3502px;width:96px;height:29px">Learn more</a>

<!-- Footer -->
<svg class="abs" style="left:33px;top:3740px" width="1135" height="449" viewBox="0 0 1135 449" preserveAspectRatio="none">
  <path d="M0 40 C240 0 420 30 620 50 C820 70 960 40 1135 10 L1135 449 L0 449Z" fill="#141a3a"/>
</svg>
<div class="abs brand" style="left:545px;top:3878px;color:#fff;font-size:24px"><span class="brand-dot" style="background:#fff"></span>Stellan</div>
<h2 class="abs" style="left:351px;top:3945px;width:500px;text-align:center;color:#fff;font-size:17px;font-weight:600">About Stellan Asset Advisors</h2>
<p class="abs footer-copy" style="top:3985px">With over 55 years of combined experience, Stellan Asset Advisors helps successful people more effectively prepare for the future.&nbsp; Our unique small team of wealth managers, financial planners and tax professionals bring you the strategies you need to preserve your wealth, minimize your taxes and create a confident retirement.&nbsp; While we’re based in Brennick County, Ohio, we serve clients nationwide.</p>
<div class="abs social" style="left:226px;top:4150px"><span></span><span></span><span></span><span></span></div>
<p class="abs" style="left:832px;top:4150px;color:#fff;font-size:9.5px">© 2021 Stellan Asset Advisors</p>
</body>
</html>
```